Morvex Business Card (intended for Business Card sized magnet)

Hi guys,

I would like to get a design for my business card for the restaurant. The design must be single sided as I intend to produce business card sized magnets.

The File attached must me on and I'm open for new ides

Can you please ensure that the design meets Cardowell's magnetic business card size specifications:

http://www.cardowell.example.au/custom-magnets.aspx?txi=15695&xnid=TopNav_Magnetic+Business+Cards+(linked+item)_Magnets_Marketing+Products&xnav=TopNav

Full Bleed Size (starting document size):
90 x 52 mm
1062 x 615 pixels
* Finished artwork should use the full bleed dimensions for best results.

Document Trim Size (final size after being cut):
87 x 49 mm
1028 x 579 pixels
* Please be sure to keep all text within the safe margin.

Resolution:
300 DPI

The winning design/source files need to meet these specifications.

Thanks
Updates

Hi guys, can I see more options please Thanks

```html
<!DOCTYPE html>
<html lang="en">
<head>
<meta charset="utf-8">
<title>Morvex Business Card – Bleed Setup</title>
<link rel="stylesheet" href="https://fonts.googleapis.com/css2?family=Cinzel:wght@400;500&family=Cormorant+Garamond:wght@400;500&family=Arimo:wght@400&display=swap">
<style>
  :root {
    --stage: #1a1e1e;
    --guide: #7fe3d2;
    --trim-red: #e30613;
    --safe-cyan: #3fd6ee;
    --card-base: #20282a;
    --photo-dark: #3a3128;
    --photo-mid: #8a7560;
    --band: #d9e2de;
    --overlay: rgba(205, 217, 212, 0.72);
    --cream: #f4ead0;
    --gold: #f3d9a4;
    --peach: #f5c7a4;
    --ink: #111;
    --brand-blue: #1f6fe0;
    --white: #ffffff;
  }
  * { margin: 0; padding: 0; box-sizing: border-box; }
  html, body { width: 1200px; height: 1000px; overflow: hidden; background: var(--stage); }
  .stage { position: relative; width: 1200px; height: 1000px; background: var(--stage); }

  .stage-title {
    position: absolute; top: 30px; left: 0; width: 100%;
    text-align: center; color: var(--white);
    font-family: "Cinzel", serif; font-weight: 400;
    font-size: 46px; letter-spacing: 3px;
  }

  .card { position: absolute; left: 246px; top: 304px; width: 708px; height: 410px; overflow: hidden; background: var(--card-base); }
  .card-photo {
    position: absolute; left: 0; top: 0; width: 300px; height: 310px;
    background: radial-gradient(circle at 40% 50%, var(--photo-mid) 0%, #6b5a48 45%, var(--photo-dark) 80%, var(--card-base) 100%);
  }
  .card-pattern { position: absolute; left: 0; top: 308px; width: 708px; height: 74px; background: var(--band); }
  .card-tagline, .card-address, .card-contact { position: absolute; right: 62px; text-align: right; white-space: nowrap; }
  .card-tagline { top: 56px; font-family: "Cinzel", serif; font-size: 19px; color: var(--gold); }
  .card-address { font-family: "Cinzel", serif; font-size: 27px; color: var(--cream); }
  .card-address.line-one { top: 78px; }
  .card-address.line-two { top: 106px; }
  .card-contact { top: 140px; font-family: "Cormorant Garamond", serif; font-size: 18px; color: var(--peach); }
  .card-name { position: absolute; left: 290px; top: 236px; font-family: "Cormorant Garamond", serif; font-size: 62px; color: var(--cream); }
  .card-web { position: absolute; left: 496px; top: 258px; font-family: "Cormorant Garamond", serif; font-size: 17px; color: var(--cream); line-height: 22px; }
  .social-mark { display: inline-block; width: 14px; height: 14px; background: var(--cream); margin-right: 6px; vertical-align: -1px; }
  .card-overlay { position: absolute; inset: 0; background: var(--overlay); }

  .guides { position: absolute; left: 0; top: 0; }

  .label-box { position: absolute; left: 357px; width: 342px; height: 39px; border: 2px solid var(--ink);
    font-family: "Arimo", sans-serif; font-size: 22px; color: var(--ink); text-align: right; padding-right: 14px; line-height: 36px; }
  .label-box.trim { top: 342px; }
  .label-box.safe { top: 396px; }
  .spec-line { position: absolute; left: 515px; top: 443px; font-family: "Arimo", sans-serif; font-size: 19px; color: var(--ink); word-spacing: 18px; }
  .guide-note { position: absolute; left: 400px; width: 400px; top: 484px; text-align: center; font-family: "Arimo", sans-serif; font-size: 17px; line-height: 22px; color: var(--ink); }
  .printer-name { position: absolute; left: 400px; width: 400px; top: 572px; text-align: center; font-family: "Arimo", sans-serif; font-size: 32px; color: var(--brand-blue); }
  .printer-disclaimer { position: absolute; left: 400px; width: 400px; top: 617px; text-align: center; font-family: "Arimo", sans-serif; font-size: 15px; line-height: 20px; color: var(--ink); }
</style>
</head>
<body>
<main class="stage">
  <h1 class="stage-title">DESIGNED WITH BLEEDS</h1>

  <section class="card" aria-label="Morvex business card">
    <div class="card-photo" role="img" aria-label="Overhead photograph of Middle Eastern dishes on a platter"></div>
    <div class="card-pattern" role="img" aria-label="Decorative geometric star pattern band"></div>
    <p class="card-tagline">Authentic Middle Eastern</p>
    <p class="card-address line-one">412 Harlow Street</p>
    <p class="card-address line-two">Westbrook North, 3190</p>
    <p class="card-contact">03 9555 0142 • morvex412@mail.example</p>
    <p class="card-name">Morvex</p>
    <p class="card-web">www.morvex.example.au<br><span class="social-mark"></span>morvexeats</p>
    <div class="card-overlay"></div>
  </section>

  <svg class="guides" width="1200" height="1000" viewBox="0 0 1200 1000" aria-hidden="true">
    <g stroke="var(--guide)" stroke-width="1">
      <line x1="246.5" y1="0" x2="246.5" y2="1000"/>
      <line x1="274.5" y1="0" x2="274.5" y2="1000"/>
      <line x1="926.5" y1="0" x2="926.5" y2="1000"/>
      <line x1="954.5" y1="0" x2="954.5" y2="1000"/>
      <line x1="0" y1="304.5" x2="1200" y2="304.5"/>
      <line x1="0" y1="332.5" x2="1200" y2="332.5"/>
      <line x1="0" y1="686.5" x2="1200" y2="686.5"/>
      <line x1="0" y1="714.5" x2="1200" y2="714.5"/>
    </g>
    <rect x="256" y="315" width="688" height="390" fill="none" stroke="var(--trim-red)" stroke-width="6"/>
    <rect x="263" y="322" width="674" height="376" fill="none" stroke="#c9d3cf" stroke-width="5"/>
    <rect x="270" y="333" width="660" height="358" fill="none" stroke="var(--safe-cyan)" stroke-width="3"/>
    <rect x="274" y="337" width="652" height="350" fill="none" stroke="var(--safe-cyan)" stroke-width="2"/>
    <rect x="726" y="356" width="120" height="8" fill="var(--trim-red)"/>
    <rect x="726" y="412" width="120" height="8" fill="var(--safe-cyan)"/>
  </svg>

  <div class="label-box trim">TRIM</div>
  <div class="label-box safe">SAFE MARGIN</div>
  <p class="spec-line">CMYK 300&nbsp;DPI</p>
  <p class="guide-note">NOTE: Before saving, turn<br>off or delete guides layer.*</p>
  <p class="printer-name">Cardowell</p>
  <p class="printer-disclaimer">*Cardowell is not responsible for guides<br>layer left in customer’s document</p>
</main>
</body>
</html>
```